Beekeeper needs a label for honey jars

Ciao! I'm from Como Italy
I'm a hobbyist beekeeper and I produce honey for myself and my friends.
I've named my apiary "Dado di sole," a play on words between my nickname (Dado, from Edoardo) and the Italian expression "Dado di sole," which translates to "a drizzle of honey" in English.
I need to create a label for my honey glass jars (250 gr and 500 gr).
I don't need a label for commercial purposes. I would like to include at least the name “Apicoltura Dado di sole", the type of honey (e.g., wildflower, acacia...) and a space for the production year, to be handwritten each year.
In the design some references to the world of bees.
For reference, attached a label with a style I like
Attached are the images of the selected jars and their measurements
Thanks and good job!

beekeeping, honey

• I would like an elegant style with clean graphics.
• Predominance of black color.

```html
<!DOCTYPE html>
<html lang="it">
<head>
<meta charset="UTF-8">
<title>Apicoltura Dado di sole – Etichetta miele</title>
<link href="https://fonts.googleapis.com/css2?family=Montserrat:wght@500&family=Great+Vibes&family=Caveat:wght@500&display=swap" rel="stylesheet">
<style>
  :root {
    --backdrop: #070605;
    --label-paper: #e6e3d8;
    --gold-script: #9c8236;
    --ink: #1f1f1c;
    --pen-blue: #3a3f9c;
    --art-sage: #9ea58e;
    --art-sage-light: #c9ccbd;
  }
  * { margin: 0; padding: 0; box-sizing: border-box; }
  html, body {
    width: 1200px;
    height: 1200px;
    overflow: hidden;
    background: var(--backdrop);
  }
  .canvas {
    position: relative;
    width: 1200px;
    height: 1200px;
  }
  .label {
    position: absolute;
    left: 190px;
    top: 165px;
    width: 820px;
    height: 870px;
    background: var(--label-paper);
    overflow: hidden;
  }
  .label__art {
    position: absolute;
    left: 120px;
    top: 190px;
    width: 620px;
    height: 480px;
    border-radius: 46% 54% 40% 60% / 50% 45% 55% 50%;
    background: radial-gradient(ellipse at 45% 40%, var(--art-sage) 0%, var(--art-sage-light) 60%, var(--label-paper) 100%);
    opacity: 0.75;
  }
  .label__name {
    position: absolute;
    left: 0;
    right: 0;
    top: 92px;
    text-align: center;
    font-family: "Montserrat", sans-serif;
    font-weight: 500;
    font-size: 46px;
    line-height: 56px;
    color: var(--ink);
  }
  .label__grade {
    position: absolute;
    left: 0;
    right: 0;
    top: 522px;
    text-align: center;
    font-family: "Montserrat", sans-serif;
    font-weight: 500;
    font-size: 29px;
    color: var(--ink);
    text-transform: uppercase;
  }
  .label__variety {
    position: absolute;
    left: 0;
    right: 0;
    top: 592px;
    text-align: center;
    font-family: "Great Vibes", cursive;
    font-size: 100px;
    line-height: 110px;
    color: var(--gold-script);
  }
  .label__claim {
    position: absolute;
    left: 0;
    right: 0;
    top: 730px;
    text-align: center;
    font-family: "Montserrat", sans-serif;
    font-weight: 500;
    font-size: 30px;
    color: var(--ink);
    text-transform: uppercase;
  }
  .label__details {
    position: absolute;
    left: 0;
    right: 0;
    top: 782px;
    display: flex;
    justify-content: center;
    align-items: flex-start;
    gap: 16px;
    font-family: "Montserrat", sans-serif;
    color: var(--ink);
  }
  .label__weight {
    font-size: 30px;
    font-weight: 500;
    line-height: 44px;
  }
  .label__date-field { display: flex; flex-direction: column; align-items: center; }
  .label__date {
    font-family: "Caveat", cursive;
    font-weight: 500;
    font-size: 44px;
    line-height: 42px;
    color: var(--pen-blue);
    border-bottom: 2px solid var(--pen-blue);
    padding: 0 4px;
  }
  .label__date-caption {
    margin-top: 5px;
    font-size: 13px;
    font-weight: 500;
    text-transform: uppercase;
    letter-spacing: 0.3px;
  }
</style>
</head>
<body>
  <main class="canvas">
    <section class="label">
      <div class="label__art" role="img" aria-label="Incisione di un'ape posata su un ramo fiorito"></div>
      <h1 class="label__name">Apicoltura Dado di sole</h1>
      <p class="label__grade">Premio Puro</p>
      <p class="label__variety">Fiore di Campo</p>
      <p class="label__claim">Miele biologico al 100%</p>
      <div class="label__details">
        <span class="label__weight">℮ 500g</span>
        <div class="label__date-field">
          <span class="label__date">01/01/2023</span>
          <span class="label__date-caption">Data di produzione</span>
        </div>
      </div>
    </section>
  </main>
</body>
</html>
```